Gentle Harbor Label

We need labels for a new brewery called "Gentle Harbor":

We need one label, that we can slightly change to suit the style of liquid. So far the beers are:
- XPA
- Pale ALe
- IPA
- Black Ale

We want creative, fun labels, nothing traditional. but appropriate to suit all international markets.

Design was promoted in LOGO & not in Design, so we got a lot of logo's but very little designs for bottles/cans.

Gentle Harbor Brewing

```html
<!DOCTYPE html>
<html lang="en">
<head>
<meta charset="utf-8">
<title>Gentle Harbor Brewing – Label Range</title>
<link rel="stylesheet" href="https://fonts.googleapis.com/css2?family=Oswald:wght@500;600&display=swap">
<style>
  :root {
    --page: #ffffff;
    --black-label: #2b2b2d;
    --black-label-edge: #3d3d3f;
    --teal-label: #3f8a9b;
    --teal-label-edge: #4f9cad;
    --orange-label: #ec9a2a;
    --orange-label-edge: #f2ad45;
    --red-label: #9b3c3a;
    --red-label-edge: #b0504c;
    --ink-grey: #d2d2d2;
    --ink-cream: #f3ecd6;
    --ink-red: #e0171b;
    --ink-teal-dark: #1f4550;
    --ink-orange-dark: #2c3a44;
    --ink-rust: #e0823d;
  }
  * { margin: 0; padding: 0; box-sizing: border-box; }
  html, body {
    width: 1200px;
    height: 835px;
    overflow: hidden;
    background: var(--page);
  }
  .label-range {
    position: relative;
    width: 1200px;
    height: 835px;
    display: flex;
    justify-content: center;
    align-items: center;
    gap: 60px;
  }
  .label {
    width: 188px;
    height: 266px;
    display: flex;
    flex-direction: column;
    align-items: center;
    padding: 42px 12px 20px;
    font-family: "Oswald", sans-serif;
    text-transform: uppercase;
    text-align: center;
  }
  .label--black  { background: linear-gradient(90deg, var(--black-label), var(--black-label-edge)); }
  .label--teal   { background: linear-gradient(90deg, var(--teal-label), var(--teal-label-edge)); }
  .label--orange { background: linear-gradient(90deg, var(--orange-label), var(--orange-label-edge)); }
  .label--red    { background: linear-gradient(90deg, var(--red-label), var(--red-label-edge)); }

  .brand-name {
    font-weight: 600;
    font-size: 27px;
    line-height: 1.02;
    letter-spacing: 0.5px;
    height: 112px;
    display: flex;
    flex-direction: column;
    justify-content: center;
  }
  .brand-name .brand-sub {
    font-size: 19px;
    letter-spacing: 3px;
  }
  .label--black  .brand-name { color: var(--ink-red); }
  .label--teal   .brand-name { color: var(--ink-cream); }
  .label--orange .brand-name { color: var(--ink-cream); }
  .label--red    .brand-name { color: var(--ink-cream); }

  .beer-style {
    margin-top: 14px;
    height: 44px;
    display: flex;
    flex-direction: column;
    justify-content: center;
    font-weight: 500;
    font-size: 16px;
    line-height: 1.1;
    letter-spacing: 2px;
  }
  .label--black .beer-style,
  .label--teal .beer-style,
  .label--red .beer-style { color: var(--ink-grey); }
  .label--orange .beer-style { color: var(--ink-cream); }

  .star-row {
    margin-top: 10px;
    display: flex;
    gap: 4px;
    align-items: center;
  }
  .star-row svg { display: block; }
  .label--black .star-row { fill: var(--ink-red); }
  .label--teal .star-row,
  .label--orange .star-row,
  .label--red .star-row { fill: var(--ink-cream); }

  .volume-note {
    margin-top: 14px;
    font-weight: 500;
    font-size: 6.5px;
    letter-spacing: 0.6px;
    color: var(--ink-cream);
  }
</style>
</head>
<body>
<main class="label-range">

  <section class="label label--black">
    <h2 class="brand-name"><span>Gentle</span><span>Harbor</span><span class="brand-sub">Brewing</span></h2>
    <p class="beer-style"><span>Black Ale</span></p>
    <div class="star-row" aria-hidden="true">
      <svg width="5" height="5" viewBox="0 0 10 10"><polygon points="5,0 6.2,3.6 10,3.6 6.9,5.8 8.1,9.5 5,7.2 1.9,9.5 3.1,5.8 0,3.6 3.8,3.6"/></svg>
      <svg width="7" height="7" viewBox="0 0 10 10"><polygon points="5,0 6.2,3.6 10,3.6 6.9,5.8 8.1,9.5 5,7.2 1.9,9.5 3.1,5.8 0,3.6 3.8,3.6"/></svg>
      <svg width="5" height="5" viewBox="0 0 10 10"><polygon points="5,0 6.2,3.6 10,3.6 6.9,5.8 8.1,9.5 5,7.2 1.9,9.5 3.1,5.8 0,3.6 3.8,3.6"/></svg>
    </div>
    <p class="volume-note">5.5%ABV - 340ML</p>
  </section>

  <section class="label label--teal">
    <h2 class="brand-name"><span>Gentle</span><span>Harbor</span><span class="brand-sub">Brewing</span></h2>
    <p class="beer-style"><span>India</span><span>Pale Ale</span></p>
    <div class="star-row" aria-hidden="true">
      <svg width="5" height="5" viewBox="0 0 10 10"><polygon points="5,0 6.2,3.6 10,3.6 6.9,5.8 8.1,9.5 5,7.2 1.9,9.5 3.1,5.8 0,3.6 3.8,3.6"/></svg>
      <svg width="7" height="7" viewBox="0 0 10 10"><polygon points="5,0 6.2,3.6 10,3.6 6.9,5.8 8.1,9.5 5,7.2 1.9,9.5 3.1,5.8 0,3.6 3.8,3.6"/></svg>
      <svg width="5" height="5" viewBox="0 0 10 10"><polygon points="5,0 6.2,3.6 10,3.6 6.9,5.8 8.1,9.5 5,7.2 1.9,9.5 3.1,5.8 0,3.6 3.8,3.6"/></svg>
    </div>
    <p class="volume-note">5.5%ABV - 340ML</p>
  </section>

  <section class="label label--orange">
    <h2 class="brand-name"><span>Gentle</span><span>Harbor</span><span class="brand-sub">Brewing</span></h2>
    <p class="beer-style"><span>Pale Ale</span></p>
    <div class="star-row" aria-hidden="true">
      <svg width="5" height="5" viewBox="0 0 10 10"><polygon points="5,0 6.2,3.6 10,3.6 6.9,5.8 8.1,9.5 5,7.2 1.9,9.5 3.1,5.8 0,3.6 3.8,3.6"/></svg>
      <svg width="7" height="7" viewBox="0 0 10 10"><polygon points="5,0 6.2,3.6 10,3.6 6.9,5.8 8.1,9.5 5,7.2 1.9,9.5 3.1,5.8 0,3.6 3.8,3.6"/></svg>
      <svg width="5" height="5" viewBox="0 0 10 10"><polygon points="5,0 6.2,3.6 10,3.6 6.9,5.8 8.1,9.5 5,7.2 1.9,9.5 3.1,5.8 0,3.6 3.8,3.6"/></svg>
    </div>
    <p class="volume-note">5.5%ABV - 340ML</p>
  </section>

  <section class="label label--red">
    <h2 class="brand-name"><span>Gentle</span><span>Harbor</span><span class="brand-sub">Brewing</span></h2>
    <p class="beer-style"><span>Extra</span><span>Pale Ale</span></p>
    <div class="star-row" aria-hidden="true">
      <svg width="5" height="5" viewBox="0 0 10 10"><polygon points="5,0 6.2,3.6 10,3.6 6.9,5.8 8.1,9.5 5,7.2 1.9,9.5 3.1,5.8 0,3.6 3.8,3.6"/></svg>
      <svg width="7" height="7" viewBox="0 0 10 10"><polygon points="5,0 6.2,3.6 10,3.6 6.9,5.8 8.1,9.5 5,7.2 1.9,9.5 3.1,5.8 0,3.6 3.8,3.6"/></svg>
      <svg width="5" height="5" viewBox="0 0 10 10"><polygon points="5,0 6.2,3.6 10,3.6 6.9,5.8 8.1,9.5 5,7.2 1.9,9.5 3.1,5.8 0,3.6 3.8,3.6"/></svg>
    </div>
    <p class="volume-note">5.5%ABV - 340ML</p>
  </section>

</main>
</body>
</html>
```